BrightPlacely.com Wordpress Theme

Hi,

I am looking for a new theme for my wordpress site. The site looks average at the moment and needs a boost. I want to have a better user experience for publishers and advertisers and the proposition for each needs to be clear with better links to registration for both.

Publisher and Advertiser sign up buttons should be on the home page.

I am leaving the brief open save I request that you use green colours on the template.

I want room to be able to add more tabs on the top level if we introduce a blog or other services.

The layout needs to be solid and please work with the copy that's already there.

see http://brightplacely.example

I am looking forward to reviewing your ideas and designs.
Updates

The button to carbon neutral cert I am going to want to make smaller and put it in the bottom of the site.

Do not go down the too fluffy green route with windmills and fuzzy clouds. I am looking for something simple, professional but also organic with a bit of zest to it. 

We are not a niche player serving ads to green only site with green only ads. We simply neutralise the effect of online advertising campaigns.

Some decent images in the header on rotation could work I am not sure. I think these would have to be abstract and largely if not totally green in colour.

Target Market(s)

BrightPlacely.com is an online ad network. Our targets are publishers and advertisers. We bring them together through providing ad serving to the network we have built on behalf of our advertisers.

Advertisers are agencys, brands, large companies looking to sell online or create awareness of the brand.

Requirements
Must have
• Please keep the site clean and use green and white
• Call to action to both publishers and advertisers to join (buttons on home page)

```html
<!DOCTYPE html>
<html lang="en">
<head>
<meta charset="utf-8">
<title>BrightPlacely.com</title>
<link href="https://fonts.googleapis.com/css2?family=Arimo:wght@400;700&display=swap" rel="stylesheet">
<style>
:root{
  --green:#3f9437;
  --green-light:#5cb24a;
  --green-dark:#2f7a28;
  --olive:#7a5a00;
  --link:#7a6512;
  --grey-bg:#e2e2e2;
  --white:#fff;
  --text-dark:#222;
}
*{margin:0;padding:0;box-sizing:border-box}
html,body{width:1200px;height:1078px;overflow:hidden}
body{position:relative;font-family:"Arimo",Arial,sans-serif;background:var(--white);color:var(--text-dark)}
.abs{position:absolute}
.site-header{left:0;top:0;width:1200px;height:146px;background:linear-gradient(#fff,#ececec)}
.brand{left:8px;top:44px;font-size:50px;font-weight:700;color:var(--green);letter-spacing:-1px}
.nav{left:528px;top:60px;display:flex;align-items:center;gap:0}
.nav a{font-size:19px;color:var(--green);text-decoration:none;margin-right:28px;line-height:40px}
.nav a.active{background:linear-gradient(var(--green-light),var(--green));color:#fff;padding:0 14px;border-radius:5px;border:1px solid #6aa22f;margin-right:24px}
.band{left:0;width:1200px;background:var(--green)}
.hero-area{left:0;top:165px;width:1200px;height:328px;background:linear-gradient(#fff,var(--grey-bg));border-left:1px solid #c9a9b0;border-right:1px solid #c9a9b0}
.hero{left:122px;top:189px;width:955px;height:278px;border:1px solid #6d8b1f;display:flex}
.hero-copy{width:706px;height:100%;background:linear-gradient(var(--green-light),var(--green));color:#fff;padding:8px 20px 0 21px}
.hero-copy h1{font-size:30px;font-weight:400;letter-spacing:-.3px;margin-bottom:6px}
.hero-copy p{font-size:13.3px;line-height:16.6px;margin-bottom:8px}
.hero-copy ul{list-style:none}
.hero-copy li{font-size:13.3px;line-height:19.6px;display:flex;align-items:center;gap:5px}
.hero-photo{flex:1;background:linear-gradient(180deg,#f4f4f4,#d9ddd8)}
.card{top:542px;height:141px;border:1px solid #cfcfcf;border-radius:6px;background:#fff}
.card h2{font-size:18.5px;font-weight:400;color:var(--olive);margin:8px 0 6px 22px}
.card ul{list-style:none;margin-left:22px}
.card li{font-size:13.5px;line-height:17.6px;color:var(--link);display:flex;align-items:center;gap:6px}
.more{position:absolute;right:30px;bottom:8px;font-size:12.5px;font-weight:700;color:var(--green-dark)}
.card p{font-size:13.3px;line-height:16.3px;color:var(--green);padding:11px 10px 0 7px}
.card p b{font-weight:700}
.footer{left:0;top:709px;width:1200px;height:320px;background:var(--green);color:#fff}
.col{top:22px}
.col h3{font-size:18.5px;font-weight:400;margin-bottom:11px}
.col p{font-size:13.3px;line-height:16.6px}
.badge{left:880px;top:208px;width:198px;height:82px;background:#fff;border-radius:8px;border:2px solid #d4d4d4}
.badge-mark{left:12px;top:10px;width:52px;height:60px;border-radius:50%;background:var(--green-light)}
.bottom{left:0;top:1029px;width:1200px;height:49px;background:linear-gradient(#fff,#e6e6e6)}
.bottom .brand-sm{left:37px;top:10px;font-size:27px;font-weight:700;color:var(--green)}
.bottom .copy{left:496px;top:18px;font-size:11.5px;color:#222}
</style>
</head>
<body>
<svg width="0" height="0" class="abs"><defs>
<symbol id="chev" viewBox="0 0 14 10"><path d="M1 1l4 4-4 4M7 1l4 4-4 4" fill="none" stroke="#8bb11f" stroke-width="2.2"/></symbol>
<symbol id="chev-w" viewBox="0 0 10 10"><path d="M1 1l4 4-4 4M5 1l4 4-4 4" fill="none" stroke="#d8ecd0" stroke-width="1.6"/></symbol>
</defs></svg>

<header class="site-header abs">
  <div class="brand abs">BrightPlacely.com</div>
  <nav class="nav abs">
    <a class="active" href="#">Advertisers</a>
    <a href="#">Publishers</a>
    <a href="#">Refarrals</a>
    <a href="#">Offsetting</a>
    <a href="#">Contact</a>
  </nav>
</header>

<div class="band abs" style="top:146px;height:19px"></div>
<section class="hero-area abs"></section>
<section class="hero abs">
  <div class="hero-copy">
    <h1>Welcome To Our Website</h1>
    <p>BrightPlacely.com is a contextual advertising network and ad exchange that brings together publishers of high quality content with advertisers, enabling them to reach their target market whilst publishers monetize their sites through advertising that's in keeping with their sites.</p>
    <ul>
      <li><svg width="10" height="10"><use href="#chev-w"/></svg>ROI tracking</li>
      <li><svg width="10" height="10"><use href="#chev-w"/></svg>Real Time Campaign Tracking &amp; Reporting</li>
      <li><svg width="10" height="10"><use href="#chev-w"/></svg>Re-Targeting</li>
      <li><svg width="10" height="10"><use href="#chev-w"/></svg>Behavioural Targeting</li>
      <li><svg width="10" height="10"><use href="#chev-w"/></svg>Geo Targeting</li>
      <li><svg width="10" height="10"><use href="#chev-w"/></svg>B2B &amp; B2C traffic</li>
      <li><svg width="10" height="10"><use href="#chev-w"/></svg>170+ content channels to target</li>
      <li><svg width="10" height="10"><use href="#chev-w"/></svg>Hundreds of millions of monthly ad impressions across ours and our partner networks</li>
    </ul>
  </div>
  <div class="hero-photo" role="img" aria-label="Photo of a smiling businessman holding a special offer sign"></div>
</section>
<div class="band abs" style="top:493px;height:29px"></div>

<section class="card abs" style="left:124px;width:208px">
  <h2>Advertisers</h2>
  <ul>
    <li><svg width="14" height="10"><use href="#chev"/></svg>Advertiser Information</li>
    <li><svg width="14" height="10"><use href="#chev"/></svg>Advertiser Login</li>
    <li><svg width="14" height="10"><use href="#chev"/></svg>Advertiser Sign Up</li>
    <li><svg width="14" height="10"><use href="#chev"/></svg>Advertising Formats</li>
  </ul>
  <span class="more">Read More</span>
</section>
<section class="card abs" style="left:347px;width:208px">
  <h2>Publishers</h2>
  <ul>
    <li><svg width="14" height="10"><use href="#chev"/></svg>Advertising Formats</li>
    <li><svg width="14" height="10"><use href="#chev"/></svg>Publisher Information</li>
    <li><svg width="14" height="10"><use href="#chev"/></svg>Publisher Login</li>
    <li><svg width="14" height="10"><use href="#chev"/></svg>Publisher Sign Up</li>
  </ul>
  <span class="more">Read More</span>
</section>
<section class="card abs" style="left:566px;width:510px">
  <p><b>BrightPlacely.com</b> collates high quality content across a range of specialist and generalist websites and blogs and equips advertisers with the tools to target visitors and optimize campaign performance.As you may have guested by our name BrightPlacely.com is both responsible and ethical 100% of the ads we serve are carbon offset meaning that you can feel good in the fact that the environmental impact of your advertising campaign has been neutralized.</p>
  <span class="more">Read More</span>
</section>

<footer class="footer abs">
  <div class="col abs" style="left:147px">
    <h3>Pages</h3>
    <p>Contact<br>Offsetting<br>Referral<br>Publishers<br>Ad Formats<br>Publisher Registration<br>Publisher Agreement<br>Advertisers<br>Ad Formats<br>Testimonials<br>Advertiser Registration<br>Advertiser Agreement</p>
  </div>
  <div class="col abs" style="left:397px">
    <h3>Publisher</h3>
    <p>BrightPlacely.<br>com offers<br>publishers to the<br>opportunity to earn<br>more income<br>through text (inline<br>text links) or by<br>displaying targeted<br>contextual adverti-<br>sing banner ads on<br>their websites or<br>blogs</p>
  </div>
  <div class="col abs" style="left:630px">
    <h3>Advertisers</h3>
    <p>BrightPlacely.com<br>can provide you access<br>to over a billion impressi-<br>ons a month to drive<br>quality traffic to your<br>website to convert. Our<br>advanced advertising<br>technology enables a<br>very high degree of tar-<br>geting to improve the<br>performance of your<br>campaigns.</p>
  </div>
  <div class="col abs" style="left:920px">
    <h3>Useful Info</h3>
    <p>Contact Us<br>Terms &amp; Conditions :<br>Advertisers<br>Terms &amp; Conditions :<br>Publishers<br>User Guide: Advertisers<br>User Guide: Publishers</p>
  </div>
  <div class="badge abs" role="img" aria-label="Carbon neutral website certificate badge"><div class="badge-mark abs"></div></div>
</footer>

<div class="bottom abs">
  <div class="brand-sm abs">BrightPlacely.com</div>
  <div class="copy abs">Copyright © 2010 BrightPlacely.com</div>
</div>
</body>
</html>
```